Blue Ridge Haulers Website (quoting web application)

We need a website designed for our furniture moving company in Cape Town, South Africa.

I have attached some logos and images for you to use.

I have also attached the layout of the three pages we want designed (pdf file)

Dark blue is our colour.

The pictures of our trucks (uploaded) epitomise the design required.

Our old site (existing) is viewable here: blueridgehaulers.co.za

Target Market(s)

People moving house in Cape Town, South Africa.

Number of Pages Required

3 page

Font styles to use
Sans Serif

Colors
0255a3

Requirements
Must have
• Page design for the 3 pages in the pdf file.

```html
<!DOCTYPE html>
<html lang="en">
<head>
<meta charset="utf-8">
<title>Blue Ridge Haulers</title>
<link href="https://fonts.googleapis.com/css2?family=Rubik:wght@400;500;700&family=Inter:wght@400;500;600;700&display=swap" rel="stylesheet">
<style>
:root{
  --navy:#323a5c;
  --green:#22d97f;
  --green-soft:#e3f6ee;
  --ink:#1f2440;
  --muted:#7c86a8;
  --page:#f6f7fb;
  --white:#ffffff;
  --blue:#3a8ee6;
  --logo:#8e97b8;
}
*{box-sizing:border-box;margin:0;padding:0}
html,body{width:1200px;height:1200px;overflow:hidden;background:#fff;font-family:"Inter",Arial,sans-serif}
.site{position:absolute;left:413px;top:0;width:399px;height:1200px;background:var(--page);overflow:hidden;color:var(--ink)}
.abs{position:absolute}
.hero-bg{left:0;top:0;width:399px;height:255px;background:var(--navy)}
.nav-item{top:10px;color:#fff;font-size:5.5px;text-align:center;line-height:1}
.nav-item small{display:block;font-size:3px;opacity:.8;margin-top:1px}
.quote-btn{left:330px;top:9px;width:32px;height:11px;background:var(--green);color:#fff;font-size:5px;display:flex;align-items:center;justify-content:center}
.hero-title{left:37px;top:67px;font-family:"Inter",sans-serif;font-style:italic;font-weight:700;font-size:11px;color:#fff}
.hero-text{left:35px;top:90px;width:116px;color:#fff;font-size:6.2px;line-height:8.3px}
.btn{background:var(--green);color:#fff;font-weight:700;display:flex;align-items:center;justify-content:center;box-shadow:0 3px 8px rgba(34,217,127,.35)}
.start-btn{left:36px;top:151px;width:56px;height:16px;font-size:4.5px}
.hero-photo{left:153px;top:48px;width:221px;height:166px;background:linear-gradient(135deg,#ffffff 0%,#eceef2 45%,#9aa0ab 70%,#2b2623 100%)}
.features{left:26px;top:225px;width:348px;height:116px;background:#fff;box-shadow:0 4px 14px rgba(40,50,90,.12)}
.feature{position:absolute;top:18px;width:90px}
.feature .icon{width:18px;height:18px;background:var(--green-soft);display:flex;align-items:center;justify-content:center}
.feature h3{font-weight:400;font-size:6.6px;margin-top:10px;letter-spacing:.1px}
.feature .rule{width:16px;height:1.5px;background:var(--green);margin-top:5px}
.feature p{font-size:3.9px;line-height:8.2px;color:var(--muted);margin-top:6px}
.plans-title{left:0;width:399px;top:398px;text-align:center;font-family:"Rubik",sans-serif;font-weight:500;font-size:11px}
.plans-sub{left:0;width:399px;top:420px;text-align:center;font-size:8px;font-weight:500}
.toggle{left:134px;top:449px;width:131px;height:16px;border:1px solid var(--green-soft);background:#fff;display:flex;font-size:3.8px;font-weight:700;letter-spacing:.6px;color:var(--green)}
.toggle span{display:flex;align-items:center;justify-content:center}
.toggle .on{width:45px;border-right:1px solid var(--green-soft)}
.toggle .off{flex:1;background:#f3fbf7;opacity:.75}
.plan{position:absolute;top:482px;width:106px;text-align:center}
.plan.featured{background:#fff;border-top:1.5px solid var(--blue);height:184px;box-shadow:0 4px 12px rgba(40,50,90,.08)}
.plan h4{font-weight:600;font-size:6.4px;margin-top:16px}
.price{font-family:"Rubik",sans-serif;font-size:19px;color:var(--green);margin-top:5px;line-height:1}
.from{font-size:3.2px;font-weight:700;margin-top:1px;margin-left:-18px}
.plan ul{list-style:none;margin-top:17px}
.plan.featured ul{margin-top:12px}
.plan li{font-size:4.6px;color:var(--muted);height:13.3px}
.plan-btn{top:634px;width:70px;height:17px;font-size:5px}
.say-band{left:174px;top:736px;width:225px;height:269px;background:var(--navy)}
.say-title{left:47px;top:756px;font-family:"Rubik",sans-serif;font-weight:700;font-size:10.5px;line-height:15.5px;color:#13204a}
.review{position:absolute;top:808px;width:117px;height:138px;padding:20px 8px 0 14px;font-size:4.4px;line-height:10px;font-weight:600}
.review.active{background:var(--green);color:#fff}
.review.plain{background:#f4f5f7;color:var(--ink)}
.review .mark{height:10px;margin-bottom:6px;display:block}
.review .who{position:absolute;left:14px;top:112px;font-size:4.6px;font-weight:700;white-space:nowrap}
.review.active .who span{color:#d7ffe9}
.review.plain .who span{color:#9aa1b5;font-weight:500}
.dots{left:205px;top:974px;display:flex;gap:4px}
.dots i{width:6px;height:6px;border-radius:50%;border:1px solid #fff;display:block}
.dots i.on{background:#fff}
.clients-label{left:0;width:399px;top:1059px;text-align:center;font-size:4.8px;font-weight:600}
.clients{left:53px;top:1078px;width:294px;display:flex;justify-content:space-between;align-items:center;font-family:"Inter",sans-serif;font-weight:700;font-size:8px;color:var(--logo)}
.copyright{left:0;width:399px;top:1143px;text-align:center;font-size:4.4px;color:var(--muted)}
.footer-links{left:0;width:399px;top:1166px;text-align:center;font-size:4.4px;color:var(--muted);word-spacing:2px}
</style>
</head>
<body>
<main class="site">
  <div class="abs hero-bg"></div>
  <nav>
    <div class="abs nav-item" style="left:152px">Home<small>page</small></div>
    <div class="abs nav-item" style="left:174px">About us<small>services</small></div>
    <div class="abs nav-item" style="left:203px">Blog<small>News</small></div>
    <div class="abs nav-item" style="left:222px">Client Area<small>Members only</small></div>
    <div class="abs nav-item" style="left:301px;top:11px">Contacts</div>
    <div class="abs quote-btn">Quote</div>
  </nav>

  <h1 class="abs hero-title">BlueRidgeHaulers</h1>
  <p class="abs hero-text">We are a professional furniture moving company offering home moves, office moves, mini moves and storage. If you need expert furniture removal in Cape Town, we are your men!</p>
  <div class="abs btn start-btn">Get Started</div>
  <div class="abs hero-photo" role="img" aria-label="Promotional banner with a white articulated truck and the company name on a diagonal blue and white layout"></div>

  <section class="abs features">
    <div class="feature" style="left:21px">
      <div class="icon"><svg width="10" height="8" viewBox="0 0 10 8"><rect x="0.5" y="0.5" width="9" height="7" fill="none" stroke="#22d97f"/><circle cx="5.5" cy="4" r="1.6" fill="none" stroke="#22d97f"/><line x1="2" y1="2" x2="2" y2="6" stroke="#22d97f"/></svg></div>
      <h3>FULLY INSURED</h3><div class="rule"></div>
      <p>We will fix or replace any furniture damaged during your Cape Town furniture removal.</p>
    </div>
    <div class="feature" style="left:131px">
      <div class="icon"><svg width="10" height="8" viewBox="0 0 10 8"><rect x="0.5" y="0.5" width="9" height="5.5" fill="none" stroke="#22d97f"/><line x1="3" y1="7.5" x2="7" y2="7.5" stroke="#22d97f"/></svg></div>
      <h3>TRAINED EXPERTS</h3><div class="rule"></div>
      <p>We have been doing your moves in Cape Town for more than 4 years.</p>
    </div>
    <div class="feature" style="left:243px">
      <div class="icon"><svg width="10" height="8" viewBox="0 0 10 8"><path d="M1 2h6l2 2-2 2H1z" fill="none" stroke="#22d97f"/><line x1="2" y1="4" x2="6" y2="4" stroke="#22d97f"/></svg></div>
      <h3>SPECIAL SERVICES</h3><div class="rule"></div>
      <p style="color:var(--ink)">We have a range of special services to make your move go smoothly.</p>
    </div>
  </section>

  <h2 class="abs plans-title">Movement Services Plans</h2>
  <p class="abs plans-sub">Please choose a plan to calculate prices</p>
  <div class="abs toggle"><span class="on">MONTHLY</span><span class="off">YEARLY - 2 MONTH FREE</span></div>

  <div class="plan" style="left:36px">
    <h4>Home Move</h4><div class="price">$10</div><div class="from">FROM</div>
    <ul><li>Free Insurance</li><li>Clean trucks</li><li>Friendly staff</li><li>Special services</li><li>Throughout Western</li></ul>
  </div>
  <div class="plan featured" style="left:147px">
    <h4>Business Move</h4><div class="price">$29</div><div class="from">FROM</div>
    <ul><li>Office relocation</li><li>Non-profit/ NGO</li><li>Film Shoot</li><li>Free Insurance</li><li>Special services</li></ul>
  </div>
  <div class="plan" style="left:258px">
    <h4>Storage</h4><div class="price">$49</div><div class="from">FROM</div>
    <ul><li>Store your items</li><li>Free Insurance</li><li>Free Collection</li><li>Enquire availability</li><li>Professional staff</li></ul>
  </div>
  <div class="abs btn plan-btn" style="left:54px">FREE QUOTE</div>
  <div class="abs btn plan-btn" style="left:164px">FREE QUOTE</div>
  <div class="abs btn plan-btn" style="left:275px">FREE QUOTE</div>

  <div class="abs say-band"></div>
  <svg class="abs" style="left:40px;top:744px" width="100" height="115" viewBox="0 0 100 115">
    <polygon points="0,0 46,0 46,70 0,115" fill="#e3f6ee" opacity=".8"/>
    <polygon points="59,0 105,0 105,70 59,115" fill="#e3f6ee" opacity=".8"/>
  </svg>
  <h2 class="abs say-title">What<br>Customers Say</h2>

  <article class="review active" style="left:119px">
    <svg class="mark" width="16" height="10" viewBox="0 0 16 10"><polygon points="0,0 5,0 3,10 0,10" fill="#fff"/><polygon points="8,0 13,0 11,10 8,10" fill="#fff"/></svg>
    <p>" It was years ago that I started working with this company.<br>I believe it was a friend who suggested Blue Ridge Haulers.<br>Since then I'm a happy customer. "</p>
    <div class="who">Daniel Mostert / <span>Kestrel Studio</span></div>
  </article>
  <article class="review plain" style="left:246px">
    <svg class="mark" width="16" height="10" viewBox="0 0 16 10"><polygon points="0,0 5,0 3,10 0,10" fill="#22d97f"/><polygon points="8,0 13,0 11,10 8,10" fill="#22d97f"/></svg>
    <p>" When I had enough of late deliveries I found out about these guys.<br>The understand your situation and help in each step of movement even packing<br>I also suggest Blue Ridge Haulers to everybody who wants ontime deliveries "</p>
    <div class="who">Pieter Naidoo / <span>Kestrel Studio</span></div>
  </article>
  <article class="review plain" style="left:374px">
    <svg class="mark" width="16" height="10" viewBox="0 0 16 10"><polygon points="0,0 5,0 3,10 0,10" fill="#22d97f"/><polygon points="8,0 13,0 11,10 8,10" fill="#22d97f"/></svg>
    <p>"Uber fast crew, great care with my things. I can only say we have had a great day"</p>
    <div class="who">Lerato</div>
  </article>
  <div class="abs dots"><i></i><i class="on"></i><i></i><i></i><i></i></div>

  <p class="abs clients-label">WHO ARE OUR CLIENTS</p>
  <div class="abs clients">
    <span>Harbourline</span><span>Tallgrass</span><span>Quillmark</span><span>Oakrow</span><span>Brightvane</span><span>Pennyfold</span>
  </div>

  <p class="abs copyright">© 2018 All Right Reserved</p>
  <p class="abs footer-links">Benefit &nbsp;/&nbsp; Pricing &nbsp;/&nbsp; Testimonials &nbsp;/&nbsp; Clients</p>
</main>
</body>
</html>
```